Business card design and logo for plumbing bussiness

We are wanting a logo for a plumbing business is Queensland Australia. KRV Plumbing and Drainage will be doing works on domestic and commercial sites.
Plumbing, drainage and gas works. We are wanting something that will stand out and be noticed. Colours could be black blue and white but open for suggestions.

Target Market(s)

Builders and home renovators

Industry/Entity Type

Plumbing

Contact Information for Business Card

Miles Dorgan - Director
0417 582 913
miles@krvplumbing.example.com.au
QBCC: 847 2106
ABN: 52 319 407 281

Font styles to use
Sans Serif

Colors
000000

Requirements
Must have
• Clear defined branding

```html
<!DOCTYPE html>
<html lang="en">
<head>
<meta charset="utf-8">
<title>KRV Plumbing and Drainage – Business Card</title>
<link href="https://fonts.googleapis.com/css2?family=Audiowide&family=Lato:wght@400;700&display=swap" rel="stylesheet">
<style>
  :root {
    --page: #e6e1da;
    --card: #121212;
    --white: #ffffff;
    --blue: #1a7fa6;
    --shadow: rgba(0,0,0,0.35);
  }
  * { margin: 0; padding: 0; box-sizing: border-box; }
  html, body { width: 1200px; height: 1200px; overflow: hidden; background: var(--page); }
  .canvas { position: relative; width: 1200px; height: 1200px; }
  .card {
    position: absolute;
    background: var(--card);
    border-radius: 16px;
    box-shadow: 0 6px 14px var(--shadow);
    overflow: hidden;
  }
  .card--front { left: 165px; top: 82px; width: 822px; height: 488px; }
  .card--back  { left: 165px; top: 602px; width: 828px; height: 488px; }

  .brand-name {
    font-family: "Audiowide", sans-serif;
    color: var(--white);
    text-transform: uppercase;
    line-height: 1.05;
    letter-spacing: 2px;
  }
  .brand-mark {
    display: inline-block;
    width: 22px; height: 22px;
    background: var(--blue);
    border-radius: 50%;
  }

  .front-logo {
    position: absolute; left: 0; right: 0; top: 178px;
    display: flex; align-items: center; justify-content: center; gap: 22px;
  }
  .front-logo .brand-name { font-size: 44px; }
  .services {
    position: absolute; left: 0; right: 0; top: 318px;
    display: flex; justify-content: center; align-items: center; gap: 16px;
    font-family: "Audiowide", sans-serif; font-size: 19px;
    color: var(--white); letter-spacing: 1px;
  }
  .services .sep { width: 3px; height: 22px; background: var(--blue); }

  .back-logo {
    position: absolute; left: 58px; top: 180px; width: 300px;
    display: flex; flex-direction: column; align-items: flex-start; gap: 16px;
  }
  .back-logo .brand-name { font-size: 36px; }
  .divider {
    position: absolute; left: 392px; top: 146px;
    width: 3px; height: 206px; background: var(--blue);
  }
  .contact { position: absolute; left: 435px; top: 128px; }
  .person-name {
    font-family: "Audiowide", sans-serif; font-size: 30px;
    color: var(--blue); letter-spacing: 1px; white-space: nowrap;
  }
  .person-role {
    font-family: "Audiowide", sans-serif; font-size: 17px;
    color: var(--white); margin: 2px 0 0 6px; letter-spacing: 1px;
  }
  .contact-list { list-style: none; margin-top: 28px; }
  .contact-list li {
    display: flex; align-items: center; gap: 12px;
    font-family: "Lato", sans-serif; font-size: 22px; color: var(--white);
    height: 28px;
  }
  .contact-list svg { width: 20px; height: 20px; flex: none; }
  .registration {
    margin-top: 16px;
    font-family: "Lato", sans-serif; font-size: 22px; color: var(--white); line-height: 1.2;
  }
</style>
</head>
<body>
<div class="canvas">

  <section class="card card--front">
    <div class="front-logo">
      <span class="brand-mark"></span>
      <span class="brand-name">KRV Plumbing<br>and Drainage</span>
    </div>
    <div class="services">
      <span>PLUMBING</span><span class="sep"></span>
      <span>DRAINAGE</span><span class="sep"></span>
      <span>GAS WORKS</span>
    </div>
  </section>

  <section class="card card--back">
    <div class="back-logo">
      <span class="brand-mark"></span>
      <span class="brand-name">KRV Plumbing<br>and Drainage</span>
    </div>
    <div class="divider"></div>
    <div class="contact">
      <div class="person-name">MILES DORGAN</div>
      <div class="person-role">DIRECTOR</div>
      <ul class="contact-list">
        <li>
          <svg viewBox="0 0 20 20" aria-hidden="true"><path d="M2 8c0-3 4-4 8-4s8 1 8 4v2h-4V8H6v2H2z M5 11h10l2 6H3z" fill="#1a7fa6"/></svg>
          0417 582 913
        </li>
        <li>
          <svg viewBox="0 0 20 20" aria-hidden="true"><rect x="1" y="4" width="18" height="12" fill="#1a7fa6"/><path d="M1 4l9 7 9-7" stroke="#121212" stroke-width="1.5" fill="none"/></svg>
          miles@krvplumbing.example.com.au
        </li>
        <li>
          <svg viewBox="0 0 20 20" aria-hidden="true"><g stroke="#1a7fa6" stroke-width="1.5" fill="none"><circle cx="10" cy="10" r="8.5"/><ellipse cx="10" cy="10" rx="4" ry="8.5"/><path d="M1.5 10h17M3 5.5h14M3 14.5h14"/></g></svg>
          krvplumbing.example.com.au
        </li>
      </ul>
      <div class="registration">
        ABN: 52 319 407 281<br>
        QBCC: 847 2106
      </div>
    </div>
  </section>

</div>
</body>
</html>
```